Snapframe Party Rentals New Business Card*

Need a business card designed for a Photo Booth Hire company.Must look very professional and colorful.A new creative logo would be a bonus. Our current logo is attached on here.

Contact Information for Business Card

Business Name: SNAPFRAME PARTY RENTALS
Contact Person: MARCUS OKAFOR
Mobile: 0491826350
Email: INFO@SNAPFRAMERENTALS.EXAMPLE
Website: WWW.SNAPFRAMERENTALS.EXAMPLE
SocialPage: WWW.SOCIALPAGE.EXAMPLE/SNAPFRAME.PARTY

Font styles to use
Serif
Sans Serif
Script

Colors

Designer to choose colors to be used in the design.

Requirements
Must have
• Bonus if the colors match our website.

```html
<!DOCTYPE html>
<html lang="en">
<head>
<meta charset="utf-8">
<title>Snapframe Party Rentals – Business Card</title>
<link rel="stylesheet" href="https://fonts.googleapis.com/css2?family=Roboto:wght@400;700;900&display=swap">
<style>
  :root {
    --canvas: #d6d6d8;
    --card-dark: #18171b;
    --card-light: #f3f3f3;
    --ink: #111111;
    --ink-soft: #2a2a2a;
    --paper-text: #ffffff;
    --rule: #c4c4c4;
  }
  * { box-sizing: border-box; margin: 0; padding: 0; }
  html, body {
    width: 1200px; height: 1015px; overflow: hidden;
    background: var(--canvas);
    font-family: "Roboto", Arial, sans-serif;
  }
  .sheet {
    width: 1200px; height: 1015px;
    display: flex; flex-direction: column; align-items: center; justify-content: center;
    gap: 40px;
  }
  .card {
    width: 780px; height: 446px;
    position: relative;
    box-shadow: 0 10px 26px rgba(0,0,0,.22);
  }
  /* Front */
  .card--front {
    background: var(--card-dark);
    color: var(--paper-text);
    display: flex; flex-direction: column; align-items: center; justify-content: center;
  }
  .brand-mark {
    display: flex; align-items: center; gap: 18px;
    margin-top: -30px;
  }
  .brand-mark__dot {
    width: 34px; height: 34px; border-radius: 50%;
    background: var(--paper-text);
    flex: none;
  }
  .brand-mark__name {
    font-weight: 900; font-size: 40px; line-height: 1.02;
    letter-spacing: 1px; text-transform: uppercase;
  }
  .card--front .website {
    position: absolute; bottom: 78px; left: 0; right: 0;
    text-align: center;
    font-size: 15px; letter-spacing: 1.5px;
  }
  /* Back */
  .card--back {
    background: var(--card-light);
    color: var(--ink);
    display: flex; align-items: center;
    padding: 0 40px 0 56px;
  }
  .back-brand {
    width: 240px; flex: none;
    display: flex; flex-direction: column; align-items: center; gap: 14px;
    text-align: center;
  }
  .back-brand__dot {
    width: 40px; height: 40px; border-radius: 50%;
    background: var(--ink);
  }
  .back-brand__name {
    font-weight: 900; font-size: 24px; line-height: 1.05;
    text-transform: uppercase; letter-spacing: .3px;
    white-space: nowrap;
  }
  .divider {
    width: 1px; height: 210px; background: var(--rule);
    margin: 0 30px 0 16px; flex: none;
  }
  .contact { display: flex; flex-direction: column; min-width: 0; }
  .contact__person {
    font-weight: 900; font-size: 30px; letter-spacing: 1px; line-height: 1.15;
  }
  .contact__phone {
    font-size: 24px; letter-spacing: 1.5px; color: var(--ink-soft);
    margin-bottom: 22px;
  }
  .contact__list { list-style: none; display: flex; flex-direction: column; gap: 9px; }
  .contact__item {
    display: flex; align-items: center; gap: 8px;
    font-size: 15px; letter-spacing: .5px; color: var(--ink-soft);
    white-space: nowrap;
  }
  .contact__icon { width: 16px; height: 16px; flex: none; }
</style>
</head>
<body>
<main class="sheet">
  <section class="card card--front" aria-label="Card front">
    <div class="brand-mark">
      <span class="brand-mark__dot"></span>
      <span class="brand-mark__name">Snapframe<br>Party Rentals</span>
    </div>
    <p class="website">WWW.SNAPFRAMERENTALS.EXAMPLE</p>
  </section>

  <section class="card card--back" aria-label="Card back">
    <div class="back-brand">
      <span class="back-brand__dot"></span>
      <span class="back-brand__name">Snapframe<br>Party Rentals</span>
    </div>
    <span class="divider"></span>
    <div class="contact">
      <h1 class="contact__person">MARCUS OKAFOR</h1>
      <p class="contact__phone">0491826350</p>
      <ul class="contact__list">
        <li class="contact__item">
          <svg class="contact__icon" viewBox="0 0 16 16" aria-hidden="true">
            <rect x="1" y="3" width="14" height="10" fill="#111"/>
            <path d="M1.5 3.8 8 9l6.5-5.2" fill="none" stroke="#f3f3f3" stroke-width="1.3"/>
          </svg>
          INFO@SNAPFRAMERENTALS.EXAMPLE
        </li>
        <li class="contact__item">
          <svg class="contact__icon" viewBox="0 0 16 16" aria-hidden="true">
            <circle cx="8" cy="8" r="7" fill="#111"/>
            <ellipse cx="8" cy="8" rx="3" ry="6.2" fill="none" stroke="#f3f3f3" stroke-width="1"/>
            <path d="M1.5 8h13" stroke="#f3f3f3" stroke-width="1"/>
          </svg>
          WWW.SNAPFRAMERENTALS.EXAMPLE
        </li>
        <li class="contact__item">
          <svg class="contact__icon" viewBox="0 0 16 16" aria-hidden="true">
            <circle cx="8" cy="8" r="7" fill="#111"/>
          </svg>
          WWW.SOCIALPAGE.EXAMPLE/SNAPFRAME.PARTY
        </li>
      </ul>
    </div>
  </section>
</main>
</body>
</html>
```